Cloud-based vaccination website

Basic website design for cloud-based medical company

Coding

Coded - Design and coding required

Number of Pages Required

1 page

Colors
3277b5

```html
<!DOCTYPE html>
<html lang="en">
<head>
<meta charset="utf-8">
<title>VAXORA – Cloud Vaccination Software</title>
<link rel="stylesheet" href="https://fonts.googleapis.com/css2?family=Catamaran:wght@400;500;600;700;800&family=Hind:wght@400;500;600&display=swap">
<style>
:root{
  --brand:#3277b5;
  --brand-deep:#1566a8;
  --brand-dark:#0d4f8a;
  --sky:#4aaeea;
  --ink:#1b1b1b;
  --text:#444;
  --muted:#9a9a9a;
  --line:#cfcfcf;
  --white:#fff;
  --black:#000;
}
*{box-sizing:border-box;margin:0;padding:0}
html,body{width:1200px;height:4367px;overflow:hidden}
body{font-family:"Hind",sans-serif;color:var(--text);background:var(--white);position:relative}
.abs{position:absolute}
h1,h2,h3,h4{font-family:"Catamaran",sans-serif;color:var(--ink)}
.accent{color:var(--brand)}
.underline{display:block;width:80px;height:4px;background:var(--brand);margin-top:10px}

/* header */
.site-header{position:absolute;left:0;top:0;width:1200px;height:103px;background:var(--white)}
.brand{position:absolute;display:flex;align-items:center;gap:10px}
.brand-mark{width:26px;height:26px;border-radius:50%;background:var(--brand)}
.brand-name{font-family:"Catamaran",sans-serif;font-weight:800;font-size:40px;color:var(--brand-dark);letter-spacing:1px;line-height:1}
.contact-item{position:absolute;top:10px;display:flex;align-items:center;gap:12px}
.contact-icon{width:40px;height:40px;border:2px solid var(--brand);border-radius:50%;display:flex;align-items:center;justify-content:center}
.contact-label{font-size:12px;color:var(--muted);line-height:1.1}
.contact-value{font-size:16px;font-weight:600;color:var(--ink);line-height:1.2}
.main-nav{position:absolute;right:105px;top:70px;display:flex;gap:28px;font-size:13px;color:var(--ink)}
.main-nav a{text-decoration:none;color:inherit;position:relative}
.main-nav a.active{color:var(--brand)}
.main-nav a.active::after{content:"";position:absolute;left:0;right:0;top:27px;height:3px;background:var(--brand)}

/* hero */
.hero{position:absolute;left:0;top:103px;width:1200px;height:610px;overflow:hidden}
.hero-photo{position:absolute;inset:0;background:linear-gradient(100deg,#c9d3da 0%,#8b9dab 35%,#6e8495 60%,#93a6b4 100%)}
.hero-title{position:absolute;left:0;width:1200px;top:170px;text-align:center;font-family:"Catamaran",sans-serif;font-weight:600;font-size:86px;letter-spacing:10px;color:var(--white);line-height:1}
.hero-text{position:absolute;left:330px;width:540px;top:262px;text-align:center;font-size:18px;color:var(--white);line-height:1.5}
.slider-arrow{position:absolute;width:66px;height:66px;border-radius:50%;border:2px solid var(--white);display:flex;align-items:center;justify-content:center}
.slider-arrow.dark{border-color:var(--white)}
.dots{position:absolute;top:576px;left:592px;display:flex;gap:7px}
.dots span{width:5px;height:5px;border-radius:50%;background:var(--white)}

.btn{position:absolute;height:50px;border-radius:25px;background:var(--brand-deep);color:var(--white);font-family:"Catamaran",sans-serif;font-weight:700;font-size:14px;display:flex;align-items:center;padding-left:16px;text-decoration:none;box-shadow:0 4px 10px rgba(0,0,0,.15)}
.btn .arr{position:absolute;right:6px;top:6px;width:38px;height:38px;border-radius:50%;background:var(--white);display:flex;align-items:center;justify-content:center}

/* about */
.about-photo{position:absolute;left:112px;top:803px;width:396px;height:396px;border-radius:50%;background:radial-gradient(circle at 45% 45%,#6fc8c4 0%,#b9d5d8 40%,#dfe6ea 75%)}
.about-badge{position:absolute;left:405px;top:1072px;width:122px;height:122px;border-radius:50%;border:5px solid var(--white);background:linear-gradient(160deg,#7fc6dd,#2f8bb8)}
.about-copy{position:absolute;left:616px;top:810px;width:440px}
.about-copy h2{font-size:34px;font-weight:600}
.para{font-size:15px;line-height:28.5px;color:var(--text)}

/* services */
.services{position:absolute;left:0;top:1278px;width:1200px;height:678px;background:linear-gradient(180deg,#1a74b7,#0f5f9f)}
.section-title{position:absolute;left:0;width:1200px;text-align:center;font-family:"Catamaran",sans-serif;font-size:36px;font-weight:700;color:var(--white)}
.section-title .light{font-weight:400}
.section-title .bar{display:block;width:80px;height:4px;background:var(--white);margin:10px auto 0}
.service-card{position:absolute;top:170px;width:308px;height:422px;background:var(--white);border-radius:10px;overflow:hidden}
.service-photo{height:350px}
.service-name{height:72px;display:flex;align-items:center;justify-content:center;font-size:19px;letter-spacing:1px;color:var(--ink)}

/* empower */
.empower{position:absolute;left:0;top:1956px;width:1200px;height:552px;background:var(--white);overflow:hidden}
.empower-photo{position:absolute;left:480px;top:0;width:720px;height:552px;background:linear-gradient(90deg,rgba(255,255,255,1) 0%,rgba(200,212,222,.6) 20%,#3f4e5c 50%,#2b3846 100%)}
.empower h2{position:absolute;left:112px;top:70px;font-size:34px;font-weight:600;line-height:39px;width:560px}
.empower h2 .accent{font-weight:400}
.empower .para{position:absolute;left:112px;top:188px;width:440px}

/* news */
.news{position:absolute;left:0;top:2508px;width:1200px;height:894px;background:linear-gradient(180deg,#4db3ee,#3ea6e6)}
.news-card{position:absolute;background:var(--white);overflow:hidden}
.date-tag{display:inline-block;background:var(--brand-deep);color:var(--white);font-family:"Catamaran",sans-serif;font-weight:700;font-size:15px;border-radius:0 20px 20px 0;padding:7px 18px}
.news-card h3{font-size:19px;font-weight:700;line-height:1.45}
.news-card p{font-size:14px;line-height:24px;color:var(--text)}
.read-link{color:var(--brand);text-decoration:underline;font-size:16px}

/* connect */
.connect h2{position:absolute;left:112px;top:3478px;font-size:50px;font-weight:700;line-height:52px;letter-spacing:1px}
.connect .intro{position:absolute;left:112px;top:3608px;width:280px;font-size:14px;line-height:24px}
.form-lead{position:absolute;left:478px;top:3478px;font-size:22px;letter-spacing:1px;color:var(--ink)}
.field{position:absolute;border:1px solid var(--line);display:flex;align-items:flex-start;padding:14px 12px;gap:10px;font-size:14px;color:var(--muted)}
.submit{position:absolute;left:480px;top:3724px;width:176px;height:51px;border-radius:26px;background:var(--brand-deep);color:var(--white);font-family:"Catamaran",sans-serif;font-weight:700;font-size:15px;display:flex;align-items:center;justify-content:center}

/* footer */
.footer-band{position:absolute;left:0;top:3956px;width:1200px;height:411px;background:var(--black)}
.footer-col h4{color:var(--white);font-size:17px;font-weight:700;letter-spacing:1px;margin-bottom:18px}
.footer-col ul{list-style:none}
.footer-col li{color:#ddd;font-size:12px;line-height:27px}
.footer-col{position:absolute;top:4040px}
.social{position:absolute;top:4113px;width:64px;height:64px;border-radius:50%;border:2px solid var(--brand);display:flex;align-items:center;justify-content:center}
.subscribe-input{position:absolute;left:748px;top:4148px;width:340px;height:48px;border-radius:24px;background:var(--white);font-size:14px;color:var(--muted);padding:14px 28px}
.footer-rule{position:absolute;left:112px;top:4297px;width:976px;height:1px;background:#333}
.copyright{position:absolute;left:112px;top:4318px;font-size:12px;color:#ddd;font-weight:600}
.legal{position:absolute;right:112px;top:4318px;font-size:12px;color:#ddd;font-weight:600;display:flex;gap:20px}
.legal span+span{border-left:1px solid #666;padding-left:20px}
</style>
</head>
<body>

<header class="site-header">
  <div class="brand" style="left:116px;top:28px">
    <span class="brand-mark"></span><span class="brand-name">VAXORA</span>
  </div>
  <div class="contact-item" style="left:598px">
    <span class="contact-icon"><svg width="18" height="18" viewBox="0 0 24 24" fill="none" stroke="#3277b5" stroke-width="2"><path d="M5 3h4l2 5-2.5 1.5a11 11 0 0 0 6 6L16 13l5 2v4a2 2 0 0 1-2 2A16 16 0 0 1 3 5a2 2 0 0 1 2-2z"/></svg></span>
    <div><div class="contact-label">Call Us</div><div class="contact-value">555 014 2290</div></div>
  </div>
  <div class="contact-item" style="left:830px">
    <span class="contact-icon"><svg width="18" height="18" viewBox="0 0 24 24" fill="none" stroke="#3277b5" stroke-width="2"><rect x="3" y="5" width="18" height="14" rx="1"/><path d="M3 6l9 7 9-7"/></svg></span>
    <div><div class="contact-label">Email</div><div class="contact-value">hello@vaxora.example</div></div>
  </div>
  <nav class="main-nav">
    <a class="active">Home</a><a>About</a><a>Services</a><a>Testimonials</a><a>News and Blog</a><a>Contact Us</a>
  </nav>
</header>

<section class="hero">
  <div class="hero-photo" role="img" aria-label="Hand touching a glowing digital medical interface with lab icons"></div>
  <h1 class="hero-title">VAXORA</h1>
  <p class="hero-text">Sed ut perspiciatis unde omnis iste natus error sit voluptatem accusantium doloremque laudantium.</p>
  <a class="btn" style="left:512px;top:332px;width:176px">GET STARTED<span class="arr"><svg width="18" height="18" viewBox="0 0 24 24" fill="none" stroke="#1566a8" stroke-width="2.5"><path d="M5 12h14M13 6l6 6-6 6"/></svg></span></a>
  <span class="slider-arrow" style="left:18px;top:243px"><svg width="18" height="18" viewBox="0 0 24 24" fill="none" stroke="#fff" stroke-width="2.5"><path d="M15 5l-7 7 7 7"/></svg></span>
  <span class="slider-arrow" style="left:1116px;top:243px"><svg width="18" height="18" viewBox="0 0 24 24" fill="none" stroke="#fff" stroke-width="2.5"><path d="M9 5l7 7-7 7"/></svg></span>
  <div class="dots"><span></span><span></span><span></span></div>
  <svg class="abs" style="left:0;top:520px" width="1200" height="90" viewBox="0 0 1200 90"><path d="M0 40 Q600 150 1200 20 L1200 90 L0 90Z" fill="#fff"/></svg>
</section>
<svg class="abs" style="left:200px;top:695px" width="810" height="50" viewBox="0 0 810 50"><path d="M0 6 Q405 60 810 4 Q405 30 0 6Z" fill="#1566a8"/></svg>

<section class="about">
  <div class="about-photo" role="img" aria-label="Hands holding a glowing molecular structure"></div>
  <div class="about-badge" role="img" aria-label="Digital security lock icon"></div>
  <div class="about-copy">
    <h2>About <span class="accent" style="font-weight:400">Us</span></h2>
    <span class="underline"></span>
    <p class="para" style="margin-top:18px">Sed ut perspiciatis unde omnis iste natus error sit voluptatem accusantium doloremque laudantium, totam rem aperiam, eaque ipsa quae ab illo inventore veritatis et quasi architecto beatae vitae dicta sunt explicabo. Nemo enim ipsam voluptatem quia voluptas sit aspernatur aut odit aut fugit, sed quia consequuntur magni dolores eos qui ratione voluptatem sequi nesciunt. Neque porro quisquam est, qui dolorem ipsum quia dolor sit amet,</p>
  </div>
  <a class="btn" style="left:616px;top:1141px;width:178px">READ MORE<span class="arr"><svg width="18" height="18" viewBox="0 0 24 24" fill="none" stroke="#1566a8" stroke-width="2.5"><path d="M5 12h14M13 6l6 6-6 6"/></svg></span></a>
</section>

<section class="services">
  <h2 class="section-title" style="top:76px">Our <span class="light">Services</span><span class="bar"></span></h2>
  <span class="slider-arrow" style="left:18px;top:350px"><svg width="18" height="18" viewBox="0 0 24 24" fill="none" stroke="#fff" stroke-width="2.5"><path d="M15 5l-7 7 7 7"/></svg></span>
  <span class="slider-arrow" style="left:1116px;top:350px"><svg width="18" height="18" viewBox="0 0 24 24" fill="none" stroke="#fff" stroke-width="2.5"><path d="M9 5l7 7-7 7"/></svg></span>
  <div class="service-card" style="left:112px"><div class="service-photo" role="img" aria-label="Woman working on medical billing at a computer" style="background:linear-gradient(160deg,#d8e3ea,#7f98ad 60%,#2b3d55)"></div><div class="service-name">MEDICAL BILLING</div></div>
  <div class="service-card" style="left:446px"><div class="service-photo" role="img" aria-label="Doctor consulting a patient through a video call" style="background:linear-gradient(160deg,#a9b7bf,#e3e6e4 50%,#c9b8a8)"></div><div class="service-name">PATIENT ENGAGEMENT</div></div>
  <div class="service-card" style="left:780px"><div class="service-photo" role="img" aria-label="Doctor with stethoscope and floating health app icons" style="background:linear-gradient(160deg,#e9edf0,#c7d3db 50%,#9fc3dd)"></div><div class="service-name">MOBILE CAPABILITIES</div></div>
</section>

<section class="empower">
  <div class="empower-photo" role="img" aria-label="Technician with a laptop walking through a server room"></div>
  <h2>Empowering your practice to focus on <span class="accent">what matters most – your patients</span></h2>
  <p class="para">Sed ut perspiciatis unde omnis iste natus error sit voluptatem accusantium doloremque laudantium, totam rem aperiam, eaque ipsa quae ab illo inventore veritatis et quasi architecto beatae vitae dicta sunt explicabo. Nemo enim ipsam voluptatem quia voluptas sit aspernatur aut odit aut fugit, sed quia consequuntur magni dolores eos qui ratione voluptatem sequi nesciunt. Neque porro quisquam est, qui dolorem ipsum quia dolor sit amet,</p>
  <a class="btn" style="left:112px;top:447px;width:178px">READ MORE<span class="arr"><svg width="18" height="18" viewBox="0 0 24 24" fill="none" stroke="#1566a8" stroke-width="2.5"><path d="M5 12h14M13 6l6 6-6 6"/></svg></span></a>
</section>

<section class="news">
  <h2 class="section-title" style="top:72px">News &amp; <span class="light">Blog</span></h2>
  <article class="news-card" style="left:112px;top:143px;width:461px;height:563px">
    <div role="img" aria-label="Hand holding a digital cloud above a stethoscope" style="height:292px;background:linear-gradient(160deg,#eef3f7,#b9cfe0 55%,#5d86a8)"></div>
    <span class="date-tag" style="margin-top:14px">DEC 04, 2020</span>
    <div style="padding:12px 30px 0 30px">
      <h3>Sedut perspiciatis unde omnis iste natus error sit voluptatem accusantium</h3>
      <p style="margin-top:10px">Sed ut perspiciatis unde omnis iste natus error sit voluptatem accusantium doloremque laudantium, totam rem aperiam, eaque ipsa quae ab illo.</p>
      <p style="margin-top:14px"><a class="read-link">Read More</a></p>
    </div>
  </article>
  <article class="news-card" style="left:627px;top:148px;width:459px;height:261px">
    <div role="img" aria-label="Doctor using a tablet" style="position:absolute;left:0;top:0;width:205px;height:261px;background:linear-gradient(160deg,#dfe8ef,#8aa4bb 60%,#3d5670)"></div>
    <div style="position:absolute;left:205px;top:16px;width:254px">
      <span class="date-tag">DEC 04, 2020</span>
      <div style="padding:8px 14px 0 14px">
        <h3 style="font-size:18px">Sedut perspiciatis...</h3>
        <p style="font-size:13px;line-height:22px">Sed ut perspiciatis unde omnis iste natus error sit voluptatem accusantium doloremque laudantium, totam rem aperiam, eaque ipsa quae ab illo.</p>
        <a class="read-link" style="font-size:13px">Read More</a>
      </div>
    </div>
  </article>
  <article class="news-card" style="left:627px;top:446px;width:459px;height:261px">
    <div role="img" aria-label="Hands holding a glowing digital human body scan" style="position:absolute;left:0;top:0;width:205px;height:261px;background:linear-gradient(160deg,#2a7fc0,#7cc8ef 50%,#1b5f96)"></div>
    <div style="position:absolute;left:205px;top:16px;width:254px">
      <span class="date-tag">DEC 04, 2020</span>
      <div style="padding:8px 14px 0 14px">
        <h3 style="font-size:18px">Sedut perspiciatis...</h3>
        <p style="font-size:13px;line-height:22px">Sed ut perspiciatis unde omnis iste natus error sit voluptatem accusantium doloremque laudantium, totam rem aperiam, eaque ipsa quae ab illo.</p>
        <a class="read-link" style="font-size:13px">Read More</a>
      </div>
    </div>
  </article>
  <a class="btn" style="left:512px;top:755px;width:176px">VIEW MORE<span class="arr"><svg width="18" height="18" viewBox="0 0 24 24" fill="none" stroke="#1566a8" stroke-width="2.5"><path d="M5 12h14M13 6l6 6-6 6"/></svg></span></a>
</section>

<section class="connect">
  <h2>CONNECT<br>US</h2>
  <p class="intro">Sed ut perspiciatis unde omnis iste natus error sit voluptatem accusantium doloremque laudantium, totam rem aperiam, eaque ipsa quae ab illo inventore veritatis et quasi architecto beatae vitae dicta sunt explicabo. Nemo enim ipsam voluptatem quia voluptas sit aspernatur aut odit aut fugit, sed quia consequuntur magni dolores eos qui ratione.</p>
  <p class="form-lead">Please feel free to contact us</p>
  <div class="field" style="left:480px;top:3525px;width:300px;height:51px"><svg width="14" height="14" viewBox="0 0 24 24" fill="#3277b5"><circle cx="12" cy="7" r="5"/><path d="M3 23a9 9 0 0 1 18 0z"/></svg>Name</div>
  <div class="field" style="left:480px;top:3590px;width:300px;height:51px"><svg width="14" height="14" viewBox="0 0 24 24" fill="none" stroke="#3277b5" stroke-width="2.5"><rect x="3" y="5" width="18" height="14"/><path d="M3 6l9 7 9-7"/></svg>Email</div>
  <div class="field" style="left:480px;top:3656px;width:300px;height:51px"><svg width="14" height="14" viewBox="0 0 24 24" fill="#3277b5"><path d="M5 2h4l2 6-3 2a12 12 0 0 0 6 6l2-3 6 2v4a2 2 0 0 1-2 2A18 18 0 0 1 3 4a2 2 0 0 1 2-2z"/></svg>Phone</div>
  <div class="field" style="left:790px;top:3525px;width:298px;height:181px"><svg width="14" height="14" viewBox="0 0 24 24" fill="none" stroke="#3277b5" stroke-width="3"><path d="M4 4l16 16"/></svg>Message</div>
  <div class="submit">SUBMIT</div>
</section>

<svg class="abs" style="left:0;top:3850px" width="1200" height="110" viewBox="0 0 1200 110"><path d="M200 44 Q600 -8 1010 42 Q600 14 200 44Z" fill="#1566a8"/><path d="M0 110 L0 100 Q600 0 1200 100 L1200 110Z" fill="#000"/></svg>
<footer class="footer-band"></footer>
<div class="brand" style="left:158px;top:4060px"><span class="brand-mark"></span><span class="brand-name" style="color:#fff;font-size:36px">VAXORA</span></div>
<span class="social" style="left:144px"><svg width="22" height="22" viewBox="0 0 24 24" fill="none" stroke="#3277b5" stroke-width="2"><path d="M5 3h4l2 5-2.5 1.5a11 11 0 0 0 6 6L16 13l5 2v4a2 2 0 0 1-2 2A16 16 0 0 1 3 5a2 2 0 0 1 2-2z"/></svg></span>
<span class="social" style="left:221px"><svg width="22" height="22" viewBox="0 0 24 24" fill="none" stroke="#3277b5" stroke-width="2"><rect x="3" y="5" width="18" height="14"/><path d="M3 6l9 7 9-7"/></svg></span>
<span class="social" style="left:298px"><svg width="18" height="18" viewBox="0 0 24 24"><rect x="3" y="3" width="18" height="18" fill="#3277b5"/></svg></span>
<div class="footer-col" style="left:421px"><h4>QUICK LINKS</h4><ul><li>Home</li><li>About</li><li>Services</li><li>Testimonials</li><li>News and Blog</li><li>Contact Us</li></ul></div>
<div class="footer-col" style="left:582px"><h4>LINKS</h4><ul><li>Terms &amp; Condition</li><li>Privacy Policy</li><li>Sitemap</li></ul></div>
<div class="footer-col" style="left:748px;width:340px"><h4>GET OUR LATEST UPDATES</h4><p style="color:#ddd;font-size:12px;line-height:26px;margin-top:-6px">Enter your mail and we'll send you all uptodate<br>latest blog and news</p></div>
<div class="subscribe-input">Enter your mail</div>
<a class="btn" style="left:748px;top:4210px;width:140px;height:40px;font-size:13px;padding-left:14px">SUBMIT<span class="arr" style="width:30px;height:30px;top:5px;right:5px"><svg width="14" height="14" viewBox="0 0 24 24" fill="none" stroke="#1566a8" stroke-width="3"><path d="M5 12h14M13 6l6 6-6 6"/></svg></span></a>
<div class="footer-rule"></div>
<p class="copyright">Copyrights ©2021. All Rights Reserved</p>
<div class="legal"><span>Privacy Policy</span><span>Cookies Policy</span></div>

</body>
</html>
```